Manuka Honey company needs a Upmarket, Luxury Website!

New Zealand, Taranaki based Manuka Honey company Marumaru Honey is looking for a new website, we are looking for an upmarket, luxury, serious website design. We export the highest quality quality Manuka Honey, straight from the Taranaki region.

Main export markets are Asia & Europe, also New Zealand & Australia.

Looking to have a beautiful, upmarket, serious, luxurious & graphical experience with mobile optimization in mind. Like the use of product staging/mockups

You can use copy from other websites to build the site and we will change the copy after the design is finished.

***Please include 'Honey Product' mockups in website.

*Will add illustrator files in coming days***

Feel free to make website functional in Shopify, Wordpress or WIX

Target Market(s)

Asia, Europe (main markets) New Zealand, Australia (Submarkets)

Coding

Coded - Design and coding required

Number of Pages Required

4 page

Requirements
Must have
• Home, Shop, About Us, Contact Us

Homepage to include:

Our Products
Company Video (video under construction)
What is MGO/UMF
Newsletter Opt-in

***(Not in Order)***

Please include 'Honey Product' mockups in website.
*Will add illustrator files in coming days
Nice to have
• FAQ & Partnership Inquiries (hyperlink in footer)

```html
<!DOCTYPE html>
<html lang="en">
<head>
<meta charset="utf-8">
<title>Marumaru Honey</title>
<link href="https://fonts.googleapis.com/css2?family=Poppins:wght@400;500;600&family=Rubik:wght@500;700;900&family=Signika:wght@400;600&display=swap" rel="stylesheet">
<style>
:root{
  --gold:#b38b4d;
  --gold-light:#c9a56a;
  --black:#000;
  --ink:#222;
  --muted:#555;
  --card:#f5f5f5;
  --line:#e3e3e3;
  --cream:#f4efe6;
  --white:#fff;
  --welcome-text:#efe6d6;
}
*{margin:0;padding:0;box-sizing:border-box}
html,body{width:1200px;height:3300px;overflow:hidden}
body{position:relative;background:var(--white);font-family:'Poppins',sans-serif;color:var(--ink)}
.abs{position:absolute}
.heading{font-family:'Signika',sans-serif;font-weight:600;color:var(--ink)}
.sub{font-size:13px;color:var(--muted);text-align:center;width:100%}

/* header */
.site-header{left:0;top:0;width:1200px;height:84px;background:var(--black);border-bottom:3px solid var(--gold)}
.brand{display:flex;align-items:center;gap:14px}
.brand-dot{width:40px;height:40px;border-radius:50%;background:var(--gold)}
.brand-name{font-family:'Poppins',sans-serif;font-weight:400;letter-spacing:3px;color:var(--gold-light);font-size:24px;white-space:nowrap}
.nav a{position:absolute;top:33px;color:#fff;font-size:13px;text-decoration:none}
.nav a.active{color:var(--gold-light)}
.caret{left:709px;top:55px;width:0;height:0;border-left:4px solid transparent;border-right:4px solid transparent;border-top:5px solid var(--gold-light)}

/* hero */
.hero{left:0;top:84px;width:1200px;height:628px;background:linear-gradient(100deg,#8a7c6a 0%,#b4a48d 35%,#c79a4a 65%,#8d5a1a 100%)}
.hero-wave{left:0;top:560px;width:520px;height:152px}
.hero-title{left:60px;top:238px;font-family:'Rubik',sans-serif;font-weight:900;font-size:66px;color:#f7d98a;letter-spacing:1px}
.hero-text{left:60px;top:318px;font-family:'Rubik',sans-serif;font-weight:700;font-size:30px;line-height:37px;color:#1b1b1b}
.btn{display:flex;align-items:center;justify-content:center;background:var(--gold);color:#fff;font-size:15px;font-weight:500;border-radius:3px}
.hero-btn{left:60px;top:447px;width:127px;height:40px}

/* products */
.card{background:var(--card)}
.card.featured{background:#fff;border:1px solid var(--line)}
.jar{border-radius:10px}
.p-title{font-size:16px;font-weight:500;text-align:center;width:100%}
.p-desc{font-size:12px;color:var(--muted);text-align:center;width:100%}
.p-price{font-size:19px;font-weight:600;color:var(--gold);text-align:center;width:100%}
.outline-btn{display:flex;align-items:center;justify-content:center;border:1.5px solid #333;border-radius:3px;font-size:15px;background:#fff}

/* welcome */
.welcome{left:0;top:1368px;width:1200px;height:450px;background:linear-gradient(90deg,#4a3a25 0%,#5e4a30 50%,#6f5737 100%)}
.welcome-text{left:151px;top:1530px;width:450px}
.welcome-text p{font-size:12px;line-height:21px;color:var(--welcome-text)}
.welcome-text p + p{margin-top:11px}
.feature{display:flex;flex-direction:column;align-items:center;justify-content:center;border-radius:50%;background:var(--gold);color:#fff;font-family:'Signika',sans-serif;font-weight:600;font-size:14px;line-height:16px;text-align:center;border:2px solid #d6b985}

/* video */
.video{left:269px;top:1988px;width:662px;height:356px;background:linear-gradient(120deg,#5e6f3b,#8e9a6a 40%,#6b4a35 80%,#3d2e22);border:3px solid #111}
.video-bar{left:0;bottom:0;width:100%;height:24px;background:#111}

/* MGO table */
.mgo{left:587px;top:2438px;width:488px;height:300px;border:1px solid var(--gold)}
.mgo-head{height:96px;background:var(--cream);position:relative}
.mgo-row{height:51px;border-top:1px solid var(--line);position:relative;font-size:12.5px}
.mgo-row span{position:absolute;top:50%;transform:translateY(-50%)}
.c1{left:22px;font-weight:500}
.c2{left:148px;font-size:11.5px;color:var(--muted);line-height:16px}
.c3{left:273px;color:var(--gold);font-size:15px;font-weight:500}
.c4{left:408px;font-size:22px;font-weight:600}

/* newsletter */
.newsletter{left:0;top:2857px;width:1200px;height:164px;background:var(--gold)}
.email{left:597px;top:2917px;width:461px;height:45px;background:#fff;border-radius:4px}

/* footer */
.footer{left:0;top:3021px;width:1200px;height:279px;background:var(--black);color:#fff}
.f-head{font-family:'Signika',sans-serif;font-weight:600;font-size:17px;color:#fff}
.f-list{list-style:none;font-size:12px;color:#cfcfcf}
.f-list li{height:22.5px;padding-left:20px;position:relative}
.f-list li::before{content:"";position:absolute;left:0;top:7px;width:4px;height:4px;border-radius:50%;background:var(--gold)}
.social{width:32px;height:32px;border:1.5px solid var(--gold);border-radius:50%}
</style>
</head>
<body>

<!-- header -->
<header class="site-header abs">
  <div class="brand abs" style="left:60px;top:20px">
    <span class="brand-dot"></span><span class="brand-name">MARUMARU HONEY</span>
  </div>
  <nav class="nav">
    <a class="active" style="left:695px">Home</a>
    <a style="left:747px">Shop</a>
    <a style="left:796px">About Us</a>
    <a style="left:864px">Contact Us</a>
    <svg class="abs" style="left:954px;top:32px" width="17" height="17" viewBox="0 0 20 20" fill="none" stroke="#c9a56a" stroke-width="1.5"><circle cx="10" cy="10" r="9"/><circle cx="10" cy="8" r="3"/><path d="M4.5 16c1.5-3 9.5-3 11 0"/></svg>
    <a style="left:980px;top:32px;font-size:12px">My Account</a>
    <a style="left:1064px;top:32px;font-size:12px">My Cart</a>
    <svg class="abs" style="left:1114px;top:28px" width="26" height="24" viewBox="0 0 26 24" fill="none" stroke="#c9a56a" stroke-width="1.5"><path d="M3 9h15l-1.5 12h-12z"/><path d="M7 9a3.5 3.5 0 0 1 7 0"/><circle cx="20" cy="7" r="5" fill="#c9a56a" stroke="none"/></svg>
  </nav>
  <span class="caret abs"></span>
</header>

<!-- hero -->
<section class="hero abs" role="img" aria-label="Photo of a honey jar with a wooden dipper and a white daisy on a wooden table"></section>
<svg class="hero-wave abs" viewBox="0 0 520 152" preserveAspectRatio="none"><path d="M0 40 C120 -10 260 10 360 70 C430 110 480 130 520 152 L0 152Z" fill="#3a2c1c" opacity=".85"/></svg>
<div class="hero-title abs">100% PURE</div>
<div class="hero-text abs">Highest Quality Quality<br>Manuka Honey, Straight From<br>The Taranaki Region.</div>
<div class="btn hero-btn abs">SHOP NOW</div>
<svg class="abs" style="left:58px;top:630px" width="112" height="44" viewBox="0 0 112 44" fill="none" stroke="#fff" stroke-width="1.5"><circle cx="21" cy="22" r="20"/><path d="M24 15l-7 7 7 7"/><circle cx="69" cy="22" r="20"/><path d="M66 15l7 7-7 7"/></svg>

<!-- products -->
<h2 class="heading abs" style="left:0;top:780px;width:1200px;text-align:center;font-size:36px">Our Products</h2>
<p class="sub abs" style="left:0;top:832px">Highest Quality Quality Manuka Honey, Straight From The Taranaki Region.</p>

<svg class="abs" style="left:118px;top:1072px" width="20" height="36" viewBox="0 0 20 36" fill="none" stroke="#333" stroke-width="1.5"><path d="M16 2L3 18l13 16"/></svg>
<svg class="abs" style="left:1062px;top:1072px" width="20" height="36" viewBox="0 0 20 36" fill="none" stroke="#333" stroke-width="1.5"><path d="M4 2l13 16L4 34"/></svg>

<article class="card abs" style="left:173px;top:926px;width:284px;height:329px">
  <div class="jar abs" style="left:91px;top:32px;width:86px;height:120px;background:linear-gradient(#c9a05a 0 12%,#3a2a30 12%)" role="img" aria-label="Dark honey jar with gold lid"></div>
  <div class="p-title abs" style="top:171px">MARUMARU HONEY</div>
  <div class="p-desc abs" style="top:193px">lorem ipsum simple text</div>
  <div class="p-price abs" style="top:222px">$25.00</div>
  <div class="outline-btn abs" style="left:78px;top:264px;width:120px;height:37px">SHOP NOW</div>
</article>

<article class="card featured abs" style="left:457px;top:888px;width:285px;height:406px">
  <svg class="abs" style="left:11px;top:15px" width="32" height="32" viewBox="0 0 32 32"><circle cx="16" cy="16" r="16" fill="#b38b4d"/><path d="M16 23l-6-6a3.5 3.5 0 0 1 6-4 3.5 3.5 0 0 1 6 4z" fill="none" stroke="#fff" stroke-width="1.5"/></svg>
  <div class="jar abs" style="left:72px;top:46px;width:134px;height:172px;background:linear-gradient(#2a2a2a 0 12%,#f2b423 12%,#e09a10)" role="img" aria-label="Glass jar of golden honey with black lid"></div>
  <div class="p-title abs" style="top:246px">MARUMARU HONEY</div>
  <div class="p-desc abs" style="top:268px">lorem ipsum simple text</div>
  <div class="p-price abs" style="top:297px">$25.00</div>
  <div class="btn abs" style="left:82px;top:339px;width:120px;height:37px">SHOP NOW</div>
</article>

<article class="card abs" style="left:742px;top:926px;width:285px;height:329px">
  <div class="jar abs" style="left:91px;top:32px;width:102px;height:120px;background:linear-gradient(#d6b06a 0 10%,#c25a1c 10%,#8a3a10)" role="img" aria-label="Amber honey jar with cream lid"></div>
  <div class="p-title abs" style="top:171px">MARUMARU HONEY</div>
  <div class="p-desc abs" style="top:193px">lorem ipsum simple text</div>
  <div class="p-price abs" style="top:222px">$25.00</div>
  <div class="outline-btn abs" style="left:80px;top:264px;width:120px;height:37px">SHOP NOW</div>
</article>

<!-- welcome -->
<section class="welcome abs" role="img" aria-label="Dimmed photo of honey being poured into a bowl"></section>
<div class="abs" style="left:153px;top:1441px;font-size:15px;color:#fff">Welcome To</div>
<h2 class="heading abs" style="left:150px;top:1466px;font-size:36px;color:var(--gold-light);font-weight:400">Marumaru Honey</h2>
<div class="welcome-text abs">
  <p>Lorem Ipsum has been the industry's standard dummy text ever since the 1500s, when an unknown printer took a galley of type and scrambled it to make a type specimen book.</p>
  <p>Lorem Ipsum has been the industry's standard dummy text ever since the 1500s, when an unknown printer took a galley of type and scrambled it to make a type specimen book. It has survived not only five centuries, but also the leap into electronic typesetting.</p>
</div>
<div class="btn abs" style="left:151px;top:1702px;width:131px;height:38px">LEARN MORE</div>

<svg class="abs" style="left:717px;top:1415px" width="360" height="360" viewBox="0 0 360 360"><circle cx="180" cy="180" r="178" fill="none" stroke="#c9a56a" stroke-width="1" stroke-dasharray="3 4" opacity=".7"/></svg>
<div class="abs" style="left:743px;top:1499px;width:301px;height:186px;border-radius:14px;background:linear-gradient(90deg,#e2962a,#2c2630 40%,#2c2630 65%,#f1ead8)" role="img" aria-label="Group of three honey jars"></div>

<div class="feature abs" style="left:702px;top:1423px;width:108px;height:108px">
  <svg width="26" height="26" viewBox="0 0 26 26" fill="none" stroke="#fff" stroke-width="1.5"><path d="M13 3c-7 6-7 14 0 20 7-6 7-14 0-20z"/><path d="M13 6v17"/></svg>100%<br>Natural</div>
<div class="feature abs" style="left:944px;top:1406px;width:136px;height:136px">
  <svg width="30" height="34" viewBox="0 0 30 34" fill="none" stroke="#fff" stroke-width="1.5"><circle cx="15" cy="12" r="10"/><circle cx="15" cy="12" r="5"/><path d="M9 20l-3 12 9-4 9 4-3-12"/></svg>Best Quality in<br>the Market</div>
<div class="feature abs" style="left:717px;top:1662px;width:108px;height:108px">
  <svg width="32" height="24" viewBox="0 0 32 24" fill="none" stroke="#fff" stroke-width="1.5"><path d="M2 4h18v13H2zM20 9h6l4 5v3h-10"/><circle cx="8" cy="19" r="2.5"/><circle cx="24" cy="19" r="2.5"/></svg>Free<br>Delivery</div>
<div class="feature abs" style="left:958px;top:1656px;width:108px;height:108px">
  <svg width="28" height="28" viewBox="0 0 28 28" fill="none" stroke="#fff" stroke-width="1.5"><path d="M26 2c-8 0-14 4-17 12l5 5c8-3 12-9 12-17z"/><path d="M9 14l-5 1 3-5M14 19l-1 5 5-3M7 21l-4 4"/></svg>Express<br>Shipping</div>

<!-- video -->
<h2 class="heading abs" style="left:0;top:1885px;width:1200px;text-align:center;font-size:36px">Watch Our Video</h2>
<p class="sub abs" style="left:0;top:1937px">Highest Quality Quality Manuka Honey, Straight From The Taranaki Region.</p>
<div class="video abs" role="img" aria-label="Video still of a beekeeper in a protective suit holding a honeycomb frame in an orchard">
  <svg class="abs" style="left:262px;top:132px" width="104" height="104" viewBox="0 0 104 104"><circle cx="52" cy="52" r="51" fill="#2a3a55" opacity=".85"/><circle cx="52" cy="52" r="42" fill="#e03221" stroke="#fff" stroke-width="4"/><path d="M44 36v32l26-16z" fill="#fff"/></svg>
  <div class="video-bar abs">
    <svg class="abs" style="left:8px;top:6px" width="640" height="12" viewBox="0 0 640 12"><rect x="2" y="1" width="2.5" height="10" fill="#fff"/><rect x="7" y="1" width="2.5" height="10" fill="#fff"/><circle cx="30" cy="6" r="3" fill="#fff"/><rect x="36" y="5" width="530" height="2" fill="#555"/><path d="M604 4h3l4-3v10l-4-3h-3z" fill="#fff"/><rect x="626" y="1" width="10" height="10" fill="none" stroke="#fff" stroke-width="1.5"/></svg>
  </div>
</div>

<!-- MGO / UMF -->
<div class="abs" style="left:0;top:2702px;width:180px;height:168px;border-radius:0 60% 50% 0;background:radial-gradient(circle at 50% 60%,#f4b231,#e39414 60%,#f6d07a)" role="img" aria-label="Honey dipper dripping onto a piece of honeycomb"></div>
<h2 class="heading abs" style="left:126px;top:2508px;font-size:36px">What Is MGO/UMF</h2>
<p class="abs" style="left:124px;top:2567px;width:420px;font-size:12.5px;line-height:21px;color:var(--muted)">MARUMARU HONEY Blends or Multifloral MARUMARU HONEY are generally cheaper and contain honey from the nectar of many flowers, or have been blended with other types of honey.</p>
<p class="abs" style="left:124px;top:2652px;font-size:12.5px;font-weight:600;color:var(--gold)">Here's how the UMF and MGO/MG ratings line up:</p>

<div class="mgo abs">
  <div class="mgo-head">
    <span class="abs" style="left:27px;top:38px;font-size:14px;font-weight:600">Strength</span>
    <span class="abs" style="left:150px;top:20px;font-size:21px">MGO(antibacterial)*</span>
    <span class="abs" style="left:182px;top:50px;font-size:14px;font-weight:500">Suggested Usage</span>
    <span class="abs" style="left:410px;top:38px;font-size:14px;font-weight:600">UMF**</span>
  </div>
  <div class="mgo-row"><span class="c1">MILD</span><span class="c2">Every Day</span><span class="c3">MGO 120+</span><span class="c4">7.5+</span></div>
  <div class="mgo-row"><span class="c1">MEDIUM</span><span class="c2">General Wellbeing</span><span class="c3">MGO 220+</span><span class="c4">10+</span></div>
  <div class="mgo-row"><span class="c1">HIGH</span><span class="c2">Digestive Health</span><span class="c3">MGO 400+</span><span class="c4">13+</span></div>
  <div class="mgo-row"><span class="c1">ULTR- HIGH</span><span class="c2">Wound Care &amp;<br>Digestive Health</span><span class="c3">MGO 900+</span><span class="c4">25+</span></div>
</div>

<!-- newsletter -->
<section class="newsletter abs"></section>
<h2 class="heading abs" style="left:140px;top:2908px;font-size:36px;color:#fff;font-weight:400">Newsletter Signup !</h2>
<p class="abs" style="left:142px;top:2958px;font-size:14px;color:#fff">Would you like to receive our eclusive update for signup !</p>
<div class="email abs">
  <span class="abs" style="left:15px;top:14px;font-size:12px;color:#555">Enter Email *</span>
  <div class="btn abs" style="left:342px;top:4px;width:115px;height:37px;font-size:15px">SUBSCRIBE</div>
</div>

<!-- footer -->
<footer class="footer abs">
  <div class="brand abs" style="left:60px;top:100px;gap:10px">
    <span class="brand-dot" style="width:30px;height:30px"></span><span class="brand-name" style="font-size:15px;letter-spacing:2px">MARUMARU HONEY</span>
  </div>
  <div class="f-head abs" style="left:300px;top:44px">Sitemap</div>
  <ul class="f-list abs" style="left:300px;top:84px"><li>Home</li><li>Shop</li><li>About Us</li><li>Contact Us</li></ul>
  <div class="f-head abs" style="left:486px;top:44px">Quick Links</div>
  <ul class="f-list abs" style="left:486px;top:84px"><li>FAQ</li><li>Partnership Inquiries</li><li>Privacy Policy</li><li>Help</li></ul>
  <div class="f-head abs" style="left:698px;top:44px">Contact Us</div>
  <svg class="abs" style="left:696px;top:82px" width="20" height="20" viewBox="0 0 20 20" fill="none" stroke="#b38b4d" stroke-width="1.3"><path d="M4 2h4l1.5 4-2.5 1.5a10 10 0 0 0 5.5 5.5L14 10.5l4 1.5v4a2 2 0 0 1-2 2A15 15 0 0 1 2 4a2 2 0 0 1 2-2z"/></svg>
  <span class="abs" style="left:729px;top:85px;font-size:12px;color:#cfcfcf">+(1) 123 456 7890</span>
  <svg class="abs" style="left:696px;top:117px" width="20" height="16" viewBox="0 0 20 16" fill="none" stroke="#b38b4d" stroke-width="1.3"><rect x="1" y="1" width="18" height="14"/><path d="M1 1l9 8 9-8"/></svg>
  <span class="abs" style="left:729px;top:117px;font-size:12px;color:#cfcfcf">info@MarumaruHoney.com</span>
  <svg class="abs" style="left:696px;top:146px" width="20" height="22" viewBox="0 0 20 22" fill="none" stroke="#b38b4d" stroke-width="1.3"><path d="M10 20s-6-6-6-11a6 6 0 0 1 12 0c0 5-6 11-6 11z"/><circle cx="10" cy="9" r="2.2"/></svg>
  <span class="abs" style="left:729px;top:148px;font-size:12px;line-height:18px;color:#cfcfcf">Marumaru Honey<br>101 – Lorem ipsum simple text</span>
  <div class="f-head abs" style="left:934px;top:44px">Follow Us</div>
  <span class="social abs" style="left:932px;top:86px"></span>
  <span class="social abs" style="left:971px;top:86px"></span>
  <span class="social abs" style="left:1010px;top:86px"></span>
  <span class="social abs" style="left:1049px;top:86px"></span>
  <div class="abs" style="left:60px;top:233px;width:1080px;height:1px;background:#333"></div>
  <p class="abs" style="left:0;top:250px;width:1200px;text-align:center;font-size:11px;color:#bbb"><span style="color:var(--gold)">©MARUMARU HONEY CO.</span>- 2021 All rights reserved.</p>
</footer>

</body>
</html>
```